Webpage for a treatment housing for young addicts.

I need a new design and files for my wordpress page. I need it to be more neat and clean. I need it to look professional with a starting page that will work as a navigation. I need like logo and phone number and such up top, a picture under it with one sentence as a slogan and under it 6 boxes to click to come to our different pages. Under it I want news etc.

Target Market(s)

Social services, employees and governements

Coding

Coded - Design and coding required

Font styles to use
Sans Serif

Colors
abd037
3176b5
9d9d9d
aaaaaa
f04a50

Requirements
Must have
• A nice design
Nice to have
• need it to look professional with a starting page that will work as a navigation. I need like logo and phone number and such up top, a picture under it with one sentence as a slogan and under it 6 boxes to click to come to our different pages. Under it I want news etc.
• today www.kolrev.se
• want more like www.tralvik.se or www.bersona.se
Should not have
• To many different colours and a messy design.

```html
<!DOCTYPE html>
<html lang="en">
<head>
<meta charset="utf-8">
<title>Kolrev – Home</title>
<link href="https://fonts.googleapis.com/css2?family=Montserrat:wght@400;500;600&family=Lato:wght@400;700&family=Playfair+Display:wght@700&display=swap" rel="stylesheet">
<style>
:root{
  --green:#85c44a;
  --green-dark:#6fae35;
  --blue:#1e8ccf;
  --text:#333333;
  --muted:#666666;
  --light-bg:#efefef;
  --topbar:#f2f2f2;
  --line:#dddddd;
  --footer:#333333;
  --white:#ffffff;
}
*{box-sizing:border-box;margin:0;padding:0}
html,body{width:1200px;height:2875px;overflow:hidden}
body{font-family:"Lato",sans-serif;color:var(--text);background:var(--white)}
.wrap{width:1046px;margin:0 auto;position:relative}

.topbar{height:46px;background:var(--topbar);font-size:15px;color:var(--text)}
.topbar .wrap{height:46px;display:flex;align-items:center;justify-content:space-between}
.social{display:flex;align-items:center;gap:0}
.social span{display:block;width:14px;height:14px;border-radius:50%;background:#333;margin:0 18px}
.social span:first-child{margin-left:0}
.social i{width:1px;height:20px;background:#ccc}
.contact-strip{display:flex;align-items:center;gap:26px}
.contact-strip div{display:flex;align-items:center;gap:10px}
.contact-strip .sep{width:1px;height:22px;background:#ccc}

.header{height:88px;background:var(--white)}
.header .wrap{height:88px;display:flex;align-items:center;justify-content:space-between}
.brand{display:flex;align-items:center;gap:10px;font-family:"Montserrat",sans-serif;font-weight:600;font-size:34px;color:var(--green)}
.brand b{width:28px;height:28px;background:var(--blue);border-radius:4px;display:block}
.nav{display:flex;gap:26px;font-family:"Lato",sans-serif;font-size:15px;text-transform:uppercase}
.nav a{color:var(--text);text-decoration:none}
.nav a.active{color:var(--green)}

.hero{height:543px;position:relative;background:linear-gradient(180deg,#6f7d86 0%,#55675c 45%,#4d6b3a 75%,#4f7a3b 100%)}
.hero h1{position:absolute;top:205px;left:0;right:0;text-align:center;font-family:"Montserrat",sans-serif;font-weight:500;font-size:50px;line-height:64px;color:var(--white);text-shadow:0 2px 6px rgba(0,0,0,.4)}

.quicklinks{height:291px;background:var(--light-bg);padding-top:73px}
.quicklinks .grid{display:grid;grid-template-columns:repeat(3,331px);column-gap:26px;row-gap:21px}
.quicklink{height:61px;background:var(--white);display:flex;align-items:center;justify-content:space-between;padding:0 13px;font-size:15px;color:var(--muted)}
.arrow{width:32px;height:32px;display:block}

.welcome{height:479px;padding-top:83px}
.welcome .wrap{display:flex;gap:18px}
.feature{width:500px;height:312px;background:var(--green);color:var(--white);text-align:center;padding-top:105px}
.feature h3{font-family:"Playfair Display",serif;font-size:36px;letter-spacing:1px}
.feature p{font-family:"Montserrat",sans-serif;font-size:23px;margin-top:18px}
.intro{flex:1;text-align:center;padding-top:32px}
.intro h2{font-family:"Montserrat",sans-serif;font-weight:600;font-size:36px;letter-spacing:1px}
.intro p{font-size:14px;line-height:25px;color:var(--muted);margin:22px auto 0;width:500px}
.btn{display:inline-block;margin-top:22px;background:var(--blue);color:var(--white);font-family:"Montserrat",sans-serif;font-weight:500;font-size:18px;padding:12px 30px;text-decoration:none}

.about{height:470px;background:var(--light-bg);padding-top:52px}
.section-title{text-align:center;font-family:"Montserrat",sans-serif;font-weight:500;font-size:36px}
.about .cards{display:flex;gap:38px;margin-top:36px}
.about-card{width:323px;background:var(--white)}
.about-card .photo{height:208px}
.about-card .label{height:62px;display:flex;align-items:center;justify-content:space-between;padding:0 13px;font-size:15px;color:var(--muted)}

.news{height:646px;padding-top:50px}
.news .layout{display:flex;gap:46px;margin-top:36px}
.news-main{width:500px;height:447px;border:1px solid var(--line)}
.news-main .photo{height:291px;background:linear-gradient(160deg,#5c7a3a,#8aa85a 45%,#c9c3b0 100%)}
.news-main h4{font-size:18px;line-height:31px;font-weight:700;margin:18px 22px 0}
.meta{font-size:13px;color:var(--muted);margin:16px 22px 0;display:flex;gap:70px}
.news-side{display:flex;flex-direction:column;gap:42px}
.news-small{width:499px;height:202px;border:1px solid var(--line);display:flex}
.news-small .photo{width:250px;height:100%}
.news-small .body{padding:38px 0 0 34px;width:240px;font-size:13px;line-height:24px;color:var(--muted)}
.news-small .rule{width:46px;height:2px;background:var(--green);margin:18px 0 14px}

.footer{height:249px;background:var(--footer);color:var(--white)}
.footer .wrap{display:flex;justify-content:space-between;padding-top:52px}
.footer .brand{font-size:34px}
.subscribe{margin-top:40px;width:291px;height:46px;border:1px solid #ccc;display:flex;align-items:center;justify-content:space-between;padding:0 18px;font-size:13px;color:#ddd}
.footer-contact{width:290px;font-size:14px;line-height:22px;padding-top:10px}
.footer-contact div{display:flex;gap:16px;align-items:flex-start;margin-bottom:20px}
.footer-contact svg{flex:none;margin-top:2px}
.copyright{height:63px;background:var(--green);text-align:center;line-height:63px;font-size:14px;color:#2f4a17}
</style>
</head>
<body>

<div class="topbar">
  <div class="wrap">
    <div class="social"><span></span><i></i><span></span><i></i><span></span></div>
    <div class="contact-strip">
      <div><svg width="16" height="16" viewBox="0 0 24 24"><path d="M6.6 10.8a15 15 0 0 0 6.6 6.6l2.2-2.2c.3-.3.7-.4 1-.2 1.1.4 2.3.6 3.6.6.6 0 1 .4 1 1V20c0 .6-.4 1-1 1A17 17 0 0 1 3 4c0-.6.4-1 1-1h3.5c.6 0 1 .4 1 1 0 1.3.2 2.5.6 3.6.1.3 0 .7-.2 1z" fill="#333"/></svg>010-4417280</div>
      <span class="sep"></span>
      <div><svg width="18" height="18" viewBox="0 0 24 24"><circle cx="12" cy="12" r="9" fill="none" stroke="#333" stroke-width="2.5"/><path d="M12 7v5l3 2" stroke="#333" stroke-width="2" fill="none"/></svg>Monday - Friday 9:00 - 18:00</div>
      <span class="sep"></span>
      <svg width="18" height="18" viewBox="0 0 24 24"><circle cx="10" cy="10" r="7" fill="none" stroke="#333" stroke-width="2.5"/><path d="M15 15l6 6" stroke="#333" stroke-width="2.5"/></svg>
    </div>
  </div>
</div>

<header class="header">
  <div class="wrap">
    <div class="brand"><b></b>Kolrev</div>
    <nav class="nav">
      <a class="active" href="#">Home</a>
      <a href="#">About Kolrev</a>
      <a href="#">Ekbacka HVB</a>
      <a href="#">Work with us</a>
      <a href="#">News</a>
      <a href="#">Plug</a>
    </nav>
  </div>
</header>

<section class="hero" role="img" aria-label="Photo of a house with a green lawn and garden">
  <h1>"We Create Sustainable<br>Roads to a Better Future"</h1>
</section>

<section class="quicklinks">
  <div class="wrap grid">
    <a class="quicklink">Therapeutic Environment The<svg class="arrow" viewBox="0 0 32 32"><circle cx="16" cy="16" r="16" fill="var(--green)"/><path d="M9 16h13M17 10l6 6-6 6" stroke="#fff" stroke-width="3" fill="none"/></svg></a>
    <a class="quicklink">The starting point of the treatment<svg class="arrow" viewBox="0 0 32 32"><circle cx="16" cy="16" r="16" fill="var(--green)"/><path d="M9 16h13M17 10l6 6-6 6" stroke="#fff" stroke-width="3" fill="none"/></svg></a>
    <a class="quicklink">Individually tailored<svg class="arrow" viewBox="0 0 32 32"><circle cx="16" cy="16" r="16" fill="var(--green)"/><path d="M9 16h13M17 10l6 6-6 6" stroke="#fff" stroke-width="3" fill="none"/></svg></a>
    <a class="quicklink">Active contact person<svg class="arrow" viewBox="0 0 32 32"><circle cx="16" cy="16" r="16" fill="var(--green)"/><path d="M9 16h13M17 10l6 6-6 6" stroke="#fff" stroke-width="3" fill="none"/></svg></a>
    <a class="quicklink">Measuring The<svg class="arrow" viewBox="0 0 32 32"><circle cx="16" cy="16" r="16" fill="var(--green)"/><path d="M9 16h13M17 10l6 6-6 6" stroke="#fff" stroke-width="3" fill="none"/></svg></a>
    <a class="quicklink">Salutogenic perspective<svg class="arrow" viewBox="0 0 32 32"><circle cx="16" cy="16" r="16" fill="var(--green)"/><path d="M9 16h13M17 10l6 6-6 6" stroke="#fff" stroke-width="3" fill="none"/></svg></a>
  </div>
</section>

<section class="welcome">
  <div class="wrap">
    <div class="feature">
      <h3>EKBACKA HVB</h3>
      <p>Treatment - in - depth description</p>
    </div>
    <div class="intro">
      <h2>WELCOME TO KOLREV</h2>
      <p>Kolrev Sverige AB carries out care and care aimed at people aged 14-25 years. This is done primarily through Home for care and housing (HVB) . We are specialists in psychosocial abuse and crime issues. By being constantly open to new methods and aware of the existing ones, we develop and improve our care. The methods are adapted to the individual...</p>
      <a class="btn" href="#">KNOW MORE</a>
    </div>
  </div>
</section>

<section class="about">
  <h2 class="section-title">ABOUT KOLREV</h2>
  <div class="wrap cards">
    <div class="about-card">
      <div class="photo" role="img" aria-label="Photo of a team gathered around a table" style="background:linear-gradient(135deg,#2e3238,#6a5a4c 55%,#c9a070)"></div>
      <div class="label">The team<svg class="arrow" viewBox="0 0 32 32"><circle cx="16" cy="16" r="16" fill="var(--blue)"/><path d="M9 16h13M17 10l6 6-6 6" stroke="#fff" stroke-width="3" fill="none"/></svg></div>
    </div>
    <div class="about-card">
      <div class="photo" role="img" aria-label="Photo of a person working carefully at a bench" style="background:linear-gradient(135deg,#7c8690,#b9b4ac 60%,#d8d4cc)"></div>
      <div class="label">Quality work<svg class="arrow" viewBox="0 0 32 32"><circle cx="16" cy="16" r="16" fill="var(--blue)"/><path d="M9 16h13M17 10l6 6-6 6" stroke="#fff" stroke-width="3" fill="none"/></svg></div>
    </div>
    <div class="about-card">
      <div class="photo" role="img" aria-label="Photo of hands joined together over a table" style="background:linear-gradient(135deg,#5a2c34,#8a6a5a 55%,#d9d2c6)"></div>
      <div class="label">Value base &amp; ethical appoach<svg class="arrow" viewBox="0 0 32 32"><circle cx="16" cy="16" r="16" fill="var(--blue)"/><path d="M9 16h13M17 10l6 6-6 6" stroke="#fff" stroke-width="3" fill="none"/></svg></div>
    </div>
  </div>
</section>

<section class="news">
  <h2 class="section-title">LATEST NEWS</h2>
  <div class="wrap layout">
    <article class="news-main">
      <div class="photo" role="img" aria-label="Photo of a house entrance covered in climbing plants and flowers"></div>
      <h4>Lorem Ipsum is simply dummy text of the printing and typesetting industry.</h4>
      <div class="meta"><span>26 Feb,2018</span><span>By,Name Surname</span></div>
    </article>
    <div class="news-side">
      <article class="news-small">
        <div class="photo" role="img" aria-label="Photo of a wooden veranda facing a garden" style="background:linear-gradient(135deg,#4f6a34,#8e6a48 55%,#c8c8c0)"></div>
        <div class="body">Lorem Ipsum is simply dummy text of the printing and typeset industry Lorem Ipsum.<div class="rule"></div>26 Feb,2018</div>
      </article>
      <article class="news-small">
        <div class="photo" role="img" aria-label="Photo of garden furniture on a patio among trees" style="background:linear-gradient(135deg,#c8d6e0,#5f7a4a 50%,#8a7a66)"></div>
        <div class="body">Lorem Ipsum is simply dummy text of the printing and typeset industry Lorem Ipsum.<div class="rule"></div>26 Feb,2018</div>
      </article>
    </div>
  </div>
</section>

<footer class="footer">
  <div class="wrap">
    <div>
      <div class="brand"><b></b>Kolrev</div>
      <div class="subscribe">Enter your email<svg width="22" height="20" viewBox="0 0 24 22"><path d="M1 11 23 1 17 21 11 14z" fill="var(--green)"/></svg></div>
    </div>
    <div class="footer-contact">
      <div><svg width="16" height="20" viewBox="0 0 16 20"><path d="M8 1a6 6 0 0 1 6 6c0 5-6 12-6 12S2 12 2 7a6 6 0 0 1 6-6z" fill="none" stroke="#fff" stroke-width="1.5"/><circle cx="8" cy="7" r="2" fill="none" stroke="#fff" stroke-width="1.5"/></svg><span>Kolrev Sverige AB<br>Lindvägen 12, 264 51 Ekby</span></div>
      <div><svg width="18" height="18" viewBox="0 0 24 24"><path d="M6.6 10.8a15 15 0 0 0 6.6 6.6l2.2-2.2c.3-.3.7-.4 1-.2 1.1.4 2.3.6 3.6.6.6 0 1 .4 1 1V20c0 .6-.4 1-1 1A17 17 0 0 1 3 4c0-.6.4-1 1-1h3.5c.6 0 1 .4 1 1 0 1.3.2 2.5.6 3.6.1.3 0 .7-.2 1z" fill="none" stroke="#fff" stroke-width="1.5"/></svg><span>010-4417280</span></div>
      <div><svg width="18" height="14" viewBox="0 0 18 14"><rect x="1" y="1" width="16" height="12" fill="none" stroke="#fff" stroke-width="1.5"/><path d="M1 1l8 7 8-7" fill="none" stroke="#fff" stroke-width="1.5"/></svg><span>info@kolrev.se</span></div>
    </div>
  </div>
</footer>
<div class="copyright">©Kolrev- 2018. All Rights Reserved.</div>

</body>
</html>
```